" Consultório odontológico diferenciado, sou formado há 28 anos, em fase de instalação, pequeno, mas com todos os equipamentos necessários para realizar odontologia de alto nível. "

```html
<!DOCTYPE html>
<html lang="pt-BR">
<head>
<meta charset="utf-8">
<title>Envelope Saco – Lumen Odontologia</title>
<link href="https://fonts.googleapis.com/css2?family=Cinzel:wght@400;500&family=Montserrat:wght@400;500&display=swap" rel="stylesheet">
<style>
  :root{
    --navy:#0f1a45;
    --navy-deep:#0a1236;
    --silver:#d9dbe2;
    --gold:#c9a24a;
    --gold-light:#f1d98a;
    --gold-dark:#8a6a22;
    --paper:#ffffff;
    --ink:#27305a;
    --stage:#c9c9cc;
    --stage-light:#ececee;
  }
  *{margin:0;padding:0;box-sizing:border-box}
  html,body{width:1200px;height:1200px;overflow:hidden}
  body{
    background:radial-gradient(ellipse at 50% 50%,var(--stage-light) 0%,#dcdcdf 55%,var(--stage) 100%);
    font-family:"Montserrat",sans-serif;
    position:relative;
  }
  .sheet-label{
    position:absolute;left:34px;top:28px;
    font-size:19px;letter-spacing:.5px;color:#3a3a3e;
  }
  .envelope{position:absolute;top:295px;height:612px;width:398px;overflow:hidden;
    box-shadow:0 6px 18px rgba(0,0,0,.18)}
  .envelope-front{left:202px;
    background:linear-gradient(180deg,var(--navy) 0%,var(--navy-deep) 100%)}
  .envelope-back{left:600px;width:396px;
    background:linear-gradient(160deg,#ffffff 0%,#f3f4f7 60%,#ffffff 100%)}
  .gold-band{position:absolute;left:0;right:0;bottom:0;height:31px;
    background:linear-gradient(180deg,var(--gold-dark) 0%,var(--gold-light) 45%,var(--gold) 70%,var(--gold-dark) 100%)}
  .brand{position:absolute;left:0;right:0;display:flex;align-items:center;justify-content:center;gap:14px}
  .brand-dot{border-radius:50%;background:var(--gold)}
  .brand-name{font-family:"Cinzel",serif;font-weight:400;letter-spacing:3px}
  .brand-sub{font-family:"Montserrat",sans-serif;letter-spacing:4px;text-transform:uppercase}
  .front-brand{top:250px;flex-direction:column;gap:6px}
  .front-brand .row{display:flex;align-items:center;gap:16px}
  .front-brand .brand-dot{width:34px;height:34px}
  .front-brand .brand-name{font-size:52px;color:var(--silver)}
  .front-brand .brand-sub{font-size:10px;color:var(--silver);margin-left:48px}
  .front-web{position:absolute;left:0;right:0;top:518px;text-align:center;
    font-size:11.5px;letter-spacing:2.4px;color:#b9bdd0}
  .flap{position:absolute;left:0;top:0;width:396px;height:56px}
  .flap-dot{position:absolute;left:186px;top:14px;width:22px;height:22px;border-radius:50%;background:var(--silver)}
  .back-brand{top:500px;left:60px}
  .back-brand .brand-dot{width:22px;height:22px}
  .back-brand .brand-name{font-size:30px;color:var(--ink)}
  .contact{position:absolute;left:0;right:0;text-align:center;font-size:9.5px;color:#333a55}
  .contact-line1{top:549px}
  .contact-line2{top:566px}
  .contact .sep{margin:0 8px;color:#9aa0b5}
</style>
</head>
<body>
  <div class="sheet-label">ENVELOPE SACO</div>

  <section class="envelope envelope-front">
    <div class="brand front-brand">
      <div class="row">
        <span class="brand-dot"></span>
        <span class="brand-name">LUMEN</span>
      </div>
      <span class="brand-sub">Odontologia</span>
    </div>
    <p class="front-web">lumenodontologia.com.br</p>
    <div class="gold-band"></div>
  </section>

  <section class="envelope envelope-back">
    <svg class="flap" viewBox="0 0 396 56" aria-hidden="true">
      <polygon points="0,0 396,0 396,56 0,56" fill="var(--navy)"/>
    </svg>
    <span class="flap-dot"></span>
    <div class="brand back-brand">
      <span class="brand-dot"></span>
      <span class="brand-name">LUMEN</span>
    </div>
    <p class="contact contact-line1">+55 11 4020-1180<span class="sep">|</span>contato@lumenodonto.com.br</p>
    <p class="contact contact-line2">R. das Acácias, 210 - Sala 14 - Jd.Aurora - CEP 04110-200 / Vila Serena-SP</p>
    <div class="gold-band"></div>
  </section>
</body>
</html>
```